Velmora Business Card

We need a design for business cards for our new company. We are a resident safety and security company company that focuses on senior living communities. we provide Nurse call, Access control, CCTV, Wired and wireless network infrastructure, Wander Management, and much more!

Our logo is the circuit board shield. Representing our high tech security solutions. I would like the business card to bring the same theme with perhaps some circuit board traces around the card similar to our logo

```html
<!DOCTYPE html>
<html lang="en">
<head>
<meta charset="utf-8">
<title>Velmora Business Card</title>
<link rel="stylesheet" href="https://fonts.googleapis.com/css2?family=Montserrat:wght@500;700&display=swap">
<style>
  :root {
    --backdrop: #2e2f31;
    --card-white: #ffffff;
    --card-navy: #0e0c24;
    --brand-blue: #1565d8;
    --accent-cyan: #1aa6f2;
    --deep-blue: #0a4fc4;
    --ink: #1a1a1a;
  }
  * { box-sizing: border-box; margin: 0; padding: 0; }
  html, body { width: 1200px; height: 675px; overflow: hidden; }
  body {
    background: var(--backdrop);
    font-family: "Montserrat", Arial, sans-serif;
    position: relative;
  }
  .card {
    position: absolute;
    top: 244px;
    width: 329px;
    height: 188px;
    overflow: hidden;
  }
  .card--front { left: 267px; background: var(--card-white); }
  .card--back { left: 604px; background: var(--card-navy); }

  .brand-name {
    position: absolute;
    left: 16px;
    top: 40px;
    font-size: 17px;
    font-weight: 700;
    color: var(--brand-blue);
    letter-spacing: 0.5px;
  }
  .brand-mark {
    position: absolute;
    left: 16px;
    top: 20px;
    width: 14px;
    height: 14px;
    border-radius: 50%;
    background: var(--brand-blue);
  }
  .holder-name {
    position: absolute;
    left: 16px;
    top: 104px;
    font-size: 11.5px;
    font-weight: 700;
    color: var(--brand-blue);
    letter-spacing: 0.6px;
  }
  .holder-title {
    position: absolute;
    left: 16px;
    top: 118px;
    font-size: 7.5px;
    font-weight: 500;
    color: var(--ink);
  }
  .contact-list {
    position: absolute;
    left: 16px;
    top: 134px;
    list-style: none;
    font-size: 7.5px;
    font-weight: 500;
    color: var(--ink);
    line-height: 10px;
  }
  .contact-list li { display: flex; align-items: center; gap: 3px; }
  .contact-list svg { width: 7px; height: 7px; fill: none; stroke: var(--brand-blue); stroke-width: 1.4; }
  .contact-list .hl { color: var(--brand-blue); }

  .shield-panel {
    position: absolute;
    top: 0;
    height: 188px;
    background: linear-gradient(160deg, var(--accent-cyan), var(--deep-blue));
  }
  .card--front .shield-panel { right: 0; width: 90px; }
  .card--back .shield-panel { left: 0; width: 92px; }

  .circuit-field {
    position: absolute;
    inset: 0;
    background: radial-gradient(ellipse at 60% 50%, #1b1840 0%, var(--card-navy) 75%);
  }
  .back-brand {
    position: absolute;
    left: 124px;
    top: 78px;
    font-size: 27px;
    font-weight: 700;
    color: var(--brand-blue);
    letter-spacing: 1px;
  }
</style>
</head>
<body>
  <section class="card card--front">
    <span class="brand-mark"></span>
    <div class="brand-name">Velmora</div>
    <div class="holder-name">JONAH PELLETIER</div>
    <div class="holder-title">President</div>
    <ul class="contact-list">
      <li><svg viewBox="0 0 10 10"><path d="M2 1 L4 3 L3 4.5 Q4.5 6.5 5.5 7 L7 6 L9 8 L7.5 9.5 Q2 8 0.5 2.5 Z"/></svg>(555) 210-4471</li>
      <li><svg viewBox="0 0 10 10"><rect x="1" y="4" width="8" height="5" rx="1"/><path d="M0.5 3 Q5 0 9.5 3"/></svg>(555) 210-4480</li>
      <li><svg viewBox="0 0 10 10"><rect x="0.8" y="2" width="8.4" height="6"/><path d="M0.8 2 L5 5.5 L9.2 2"/></svg>jonah@velmora.com</li>
      <li><svg viewBox="0 0 10 10"><circle cx="5" cy="5" r="4"/><path d="M1 5 H9 M5 1 Q2.5 5 5 9 M5 1 Q7.5 5 5 9"/></svg>www.<span class="hl">velmora</span>.com</li>
    </ul>
    <div class="shield-panel" role="img" aria-label="Large blue brand emblem decoration, left half"></div>
  </section>

  <section class="card card--back">
    <div class="circuit-field" role="img" aria-label="Dark navy circuit board trace pattern"></div>
    <div class="shield-panel" role="img" aria-label="Large blue brand emblem decoration, right half"></div>
    <div class="back-brand">Velmora</div>
  </section>
</body>
</html>
```